Keeep it up is our company motto. Need "keeep it up" sticker design for promotional pur...

I need a sticker design for my upstart company called Plumvex which I like to describe as The Friendly Tovari Pal of Personal Growth. I'm looking for a cleanly designed combination mark that joins together our logo (see uploaded file) and the phrase "keeep it up." The 3 E's stand for Everyday Earnest Effort. One or two colors maximum. The phrase may be split up vertically or horizontally and the logo may also be tweaked a bit if needed. Overall design should be simple and easily recognizable.

```html
<!DOCTYPE html>
<html lang="en">
<head>
<meta charset="utf-8">
<title>Plumvex – Keeep It Up Sticker</title>
<link rel="stylesheet" href="https://fonts.googleapis.com/css2?family=Rubik+Dirt&display=swap">
<style>
  :root {
    --backdrop: #2b2b2b;
    --sticker-edge: #000000;
    --sticker-yellow: #fff200;
    --ink: #1a1a1a;
  }
  html, body {
    margin: 0;
    padding: 0;
    width: 1200px;
    height: 997px;
    overflow: hidden;
    background: var(--backdrop);
  }
  .canvas {
    position: relative;
    width: 1200px;
    height: 997px;
  }
  .sticker {
    position: absolute;
    left: 270px;
    top: 260px;
    width: 667px;
    height: 447px;
    background: var(--sticker-edge);
  }
  .sticker-face {
    position: absolute;
    left: 30px;
    top: 27px;
    width: 605px;
    height: 393px;
    background: var(--sticker-yellow);
  }
  .brand-mark {
    position: absolute;
    width: 134px;
    height: 40px;
    margin-left: -67px;
    margin-top: -20px;
    text-align: center;
    line-height: 40px;
    font-family: "Rubik Dirt", sans-serif;
    font-size: 25px;
    color: var(--ink);
    letter-spacing: 1px;
  }
  .motto-line {
    position: absolute;
    left: 172px;
    top: 138px;
    margin: 0;
    font-family: "Rubik Dirt", sans-serif;
    font-size: 58px;
    line-height: 1;
    color: var(--ink);
    letter-spacing: 1px;
    white-space: nowrap;
  }
  .motto-up {
    position: absolute;
    left: 172px;
    top: 186px;
    margin: 0;
    font-family: "Rubik Dirt", sans-serif;
    font-size: 200px;
    line-height: 1;
    color: var(--ink);
    letter-spacing: -4px;
  }
</style>
</head>
<body>
  <main class="canvas">
    <section class="sticker" aria-label="Keeep it up sticker">
      <div class="sticker-face">
        <span class="brand-mark" style="left:75px;top:63px">PLUMVEX</span>
        <span class="brand-mark" style="left:230px;top:63px">PLUMVEX</span>
        <span class="brand-mark" style="left:387px;top:63px">PLUMVEX</span>
        <span class="brand-mark" style="left:527px;top:63px">PLUMVEX</span>

        <span class="brand-mark" style="left:75px;top:158px">PLUMVEX</span>
        <span class="brand-mark" style="left:75px;top:253px">PLUMVEX</span>
        <span class="brand-mark" style="left:75px;top:343px">PLUMVEX</span>

        <span class="brand-mark" style="left:527px;top:158px">PLUMVEX</span>
        <span class="brand-mark" style="left:527px;top:253px">PLUMVEX</span>
        <span class="brand-mark" style="left:527px;top:343px">PLUMVEX</span>

        <p class="motto-line">KEEEP IT</p>
        <p class="motto-up">UP</p>
      </div>
    </section>
  </main>
</body>
</html>
```